Design a beautiful onepager menu for a restaurant

We need a onepager for a big italian restaurant.
On this onepager, there are 3 special offers for lunch time.

>> size should be DIN A 4 (use the template, all important designs need to be in white field)
>> 2-sided: front side is with full design, back side is in a matching color
>> At the end I need the print-ready jpeg and also the open file
>> the used font is source sans pro

We already have a corporate identity and a menu card (see attached).
The new onepager can look different, because it is a special offer and should attract attention!
But consider to keep our corporate identity.
We also have a rough idea for the onepager, but you can do it different if you want!
See also the text content attached. (language: german) If you don't understand the meaning, pls translate it for yourself!

Let me know any questions!

EDIT: PLEASE BEAR IN MIND TO KEEP THE COPORATE IDENTITY / KEEP THE OLD DESIGN FROM THE REFERENCES!!!!

```html
<!DOCTYPE html>
<html lang="de">
<head>
<meta charset="utf-8">
<title>Solentino – Mittagsmenü</title>
<link rel="stylesheet" href="https://fonts.googleapis.com/css2?family=Source+Sans+3:wght@400;600&display=swap">
<style>
  :root {
    --stage: #8d8d8f;
    --paper: #ffffff;
    --sun: #f5e400;
    --sun-pale: #f8f0a0;
    --slate: #5c5a5e;
    --ink: #1e1e1e;
    --brand: #9a3a1c;
    --badge: #1a1a1a;
    --wood-dark: #2e1e14;
    --wood-mid: #5a3a24;
  }
  * { margin: 0; padding: 0; box-sizing: border-box; }
  html, body { width: 1200px; height: 941px; overflow: hidden; }
  body {
    background: var(--stage);
    font-family: "Source Sans 3", sans-serif;
    color: var(--ink);
    position: relative;
  }
  .page {
    position: absolute;
    top: 169px;
    height: 606px;
    background: var(--paper);
    overflow: hidden;
  }
  .page-front { left: 167px; width: 394px; }
  .page-back { left: 631px; width: 436px; }
  .page svg.frame { position: absolute; inset: 0; width: 100%; height: 100%; }

  /* front */
  .food-photo {
    position: absolute; left: 0; top: 225px; width: 394px; height: 381px;
    background: radial-gradient(ellipse at 40% 55%, #8a4a2a 0%, var(--wood-mid) 40%, var(--wood-dark) 100%);
  }
  .tab-label {
    position: absolute; top: 42px; left: 80px; width: 235px;
    text-align: center; font-size: 13px;
  }
  .brand-name {
    position: absolute; top: 82px; left: 80px; width: 235px;
    text-align: center; font-size: 38px; font-weight: 600; color: var(--brand);
    letter-spacing: 1px;
  }
  .hours {
    position: absolute; top: 157px; left: 80px; width: 235px;
    text-align: center; font-size: 13px;
  }
  .dine-in-badge {
    position: absolute; left: 220px; top: 340px; width: 168px; height: 62px;
    background: var(--badge); color: var(--paper);
    transform: rotate(-14deg); border-radius: 6px;
    font-size: 17px; line-height: 1.1; text-align: center;
    display: flex; align-items: center; justify-content: center;
    padding: 4px 10px;
  }

  /* back */
  .offer-title {
    position: absolute; font-size: 25px; white-space: pre;
  }
  .offer-line { position: absolute; font-size: 14px; }
  .offer-pizza { left: 92px; top: 24px; }
  .pizza-size { left: 92px; top: 64px; }
  .pizza-low { left: 92px; top: 98px; }
  .pizza-high { left: 92px; top: 132px; }
  .dish-photo {
    position: absolute; border-radius: 50%;
  }
  .dish-pizza {
    left: 346px; top: 63px; width: 66px; height: 66px;
    background: radial-gradient(circle, #e2882f 0%, #b5461e 60%, #7a3a18 100%);
    outline: 2px dashed #bbb; outline-offset: 3px;
  }
  .dish-burger {
    left: 277px; top: 491px; width: 72px; height: 72px;
    background: radial-gradient(circle, #c98a3a 0%, #7a3a18 60%, #2a1a10 100%);
  }
  .drink-title { left: 136px; top: 219px; font-size: 16px; white-space: pre; position: absolute; }
  .drink-note {
    position: absolute; left: 136px; top: 294px; width: 140px;
    font-size: 7.5px; line-height: 2.2;
  }
  .offer-burger { left: 15px; top: 456px; }
  .burger-note { left: 33px; top: 506px; }
</style>
</head>
<body>

<section class="page page-front">
  <div class="food-photo" role="img" aria-label="Gegrilltes Steak mit Gemüse und Spießen auf einem Holzbrett"></div>
  <svg class="frame" viewBox="0 0 394 606" aria-hidden="true">
    <path d="M0 0H394V240C394 285 250 285 197 345C144 285 0 285 0 240Z" fill="var(--sun)"/>
    <path d="M16 0H378V232C378 268 240 272 197 322C154 272 16 268 16 232Z" fill="var(--paper)"/>
    <path d="M30 0H364V222C364 255 232 262 197 302C162 262 30 255 30 222Z" fill="var(--slate)"/>
    <path d="M40 0H354V215C354 245 228 252 197 288C166 252 40 245 40 215Z" fill="var(--paper)"/>
    <path d="M92 33H303L315 45V65H80V45Z" fill="var(--sun)"/>
    <path d="M80 140H315V180C315 195 230 195 197 215C164 195 80 195 80 180Z" fill="var(--sun)"/>
  </svg>
  <div class="tab-label">Mittagsmenü</div>
  <div class="brand-name">Solentino</div>
  <div class="hours">Mo – Fr. 11 – 14 Uhr</div>
  <div class="dine-in-badge">Nur gültig bei Verzehr im Restaurant</div>
</section>

<section class="page page-back">
  <svg class="frame" viewBox="0 0 436 606" aria-hidden="true">
    <path d="M14 0C75 80 78 190 0 236" fill="none" stroke="var(--sun)" stroke-width="16"/>
    <path d="M0 26C44 92 44 168 0 206" fill="none" stroke="var(--slate)" stroke-width="12"/>
    <circle cx="418" cy="237" r="25" fill="var(--sun-pale)"/>
    <circle cx="25" cy="384" r="27" fill="var(--sun-pale)"/>
    <rect x="124" y="192" width="161" height="235" rx="8" fill="var(--sun)"/>
    <path d="M124 217H90Q73 217 73 234V340Q73 357 90 357H124V337H100Q93 337 93 330V244Q93 237 100 237H124Z" fill="var(--sun)"/>
    <path d="M436 330C380 360 360 430 380 606" fill="none" stroke="var(--sun)" stroke-width="18"/>
    <path d="M436 362C402 392 396 452 406 606" fill="none" stroke="var(--slate)" stroke-width="14"/>
  </svg>

  <div class="offer-title offer-pizza">Jede Pizza     ab 4 €</div>
  <div class="offer-line pizza-size">Größe „normal“</div>
  <div class="offer-line pizza-low">Alle Pizzen unter 6,50 € für nur 4€.</div>
  <div class="offer-line pizza-high">Alle Pizzen ab 6,50 für nur 5€.</div>
  <div class="dish-photo dish-pizza" role="img" aria-label="Pizza von oben"></div>

  <div class="drink-title">1 Getränk     gratis</div>
  <div class="drink-note">Gilt für alle Pasta Gerichte &amp; Aufläufe.<br>Cola, Cola light, Orangenlimo oder Zitronenlimo 0,3 l</div>

  <div class="offer-title offer-burger">Jedes Burger Menü     - 1,50 €</div>
  <div class="offer-line burger-note">Nur gültig für Bürger Menüs.</div>
  <div class="dish-photo dish-burger" role="img" aria-label="Burger mit Käse und Salat"></div>
</section>

</body>
</html>
```